Window company needs new banner

Window company that has 3 focuses needs a new banner ad.

We sell window hardware
We make new sashes and windows
We restore old windows

http://www.tlsashandrenewal.com

I would like to create a new banner ad for our home page. The ad would try to capture the 3 sections listed above. I would also say they are listed in importance. Our main focus is hardware for this ad.

our best pictures are on our website.

Our suppliers websites
http://www.brindle.co.uk
http://www.kelphardware.co.uk
https://www.pellowgoods.com

Target Market(s)

Historical buildings
Restoration contractors
window restorers
DIY home owners
custom window and door fabricators- Trades people

Industry/Entity Type

Home And Garden

Font styles to use
Serif

Requirements
Must have
• Show the high level of quality of our hardware and other services

```html
<!DOCTYPE html>
<html lang="en">
<head>
<meta charset="utf-8">
<title>Trueline Sash &amp; Renewal — Banner Set</title>
<link rel="stylesheet" href="https://fonts.googleapis.com/css2?family=Cormorant+SC:wght@600;700&family=Cormorant+Garamond:wght@500;600&display=swap">
<style>
  :root {
    --stage-inner: #2a2a2a;
    --stage-outer: #0f0f0f;
    --header-dark: #1e1a17;
    --panel-white: #ffffff;
    --ink: #1b1b1b;
    --accent-red: #d8141c;
    --button-red-top: #e0252a;
    --button-red-bottom: #8a0a0c;
    --button-grey-top: #e6e6e6;
    --button-grey-bottom: #8f8f8f;
    --brand-grey: #d9d9d9;
    --brass-light: #f6e48a;
    --brass-mid: #d9b640;
    --brass-dark: #9c7a1c;
    --label: #b8b8b8;
  }
  * { margin: 0; padding: 0; box-sizing: border-box; }
  html, body { width: 1200px; height: 1000px; overflow: hidden; }
  body {
    position: relative;
    background: radial-gradient(ellipse at 50% 42%, var(--stage-inner) 0%, #1c1c1c 45%, var(--stage-outer) 100%);
    font-family: "Cormorant SC", "Times New Roman", serif;
  }
  .banner {
    position: absolute;
    overflow: hidden;
    background: var(--panel-white);
    box-shadow: 0 6px 14px rgba(0,0,0,.75);
  }
  .banner-header { position: absolute; background: var(--header-dark); }
  .brand {
    position: absolute;
    display: flex;
    align-items: center;
    gap: 6px;
    color: var(--brand-grey);
    font-family: "Cormorant SC", serif;
    font-weight: 600;
    white-space: nowrap;
    transform: translateX(-50%);
  }
  .brand-mark { width: 20px; height: 20px; background: var(--accent-red); flex: none; }
  .brand-name { font-size: 17px; line-height: 1; letter-spacing: .3px; }
  .product {
    position: absolute;
    border-radius: 6px;
    background: radial-gradient(ellipse at 40% 35%, var(--brass-light) 0%, var(--brass-mid) 55%, var(--brass-dark) 100%);
  }
  .headline {
    position: absolute;
    transform: translateX(-50%);
    text-align: center;
    color: var(--ink);
    font-weight: 700;
    white-space: nowrap;
  }
  .headline .accent { color: var(--accent-red); }
  .cta {
    position: absolute;
    display: flex;
    align-items: center;
    justify-content: center;
    border-radius: 7px;
    font-weight: 700;
    font-size: 17px;
  }
  .cta-red {
    background: linear-gradient(var(--button-red-top), var(--button-red-bottom));
    color: #fff;
    text-shadow: 0 1px 1px rgba(0,0,0,.5);
  }
  .cta-grey {
    background: linear-gradient(var(--button-grey-top), var(--button-grey-bottom));
    color: var(--ink);
  }
  .size-label {
    position: absolute;
    transform: translateX(-50%);
    color: var(--label);
    font-family: "Cormorant Garamond", serif;
    font-weight: 600;
    font-size: 16px;
  }
</style>
</head>
<body>

  <!-- Skyscraper 160x600 -->
  <section class="banner banner-skyscraper" style="left:236px; top:105px; width:160px; height:600px;">
    <div class="banner-header" style="left:0; top:0; width:160px; height:99px;">
      <div class="brand" style="left:80px; top:38px; flex-direction:column; gap:5px;">
        <span class="brand-mark"></span>
        <span class="brand-name" style="font-size:15px;">Trueline Sash</span>
      </div>
    </div>
    <div class="product" role="img" aria-label="Polished brass sash window lock with screws" style="left:10px; top:125px; width:144px; height:95px;"></div>
    <div class="product" role="img" aria-label="Polished brass door knob on round rose" style="left:24px; top:235px; width:112px; height:82px; border-radius:40px;"></div>
    <div class="product" role="img" aria-label="Brass sash lift, latch and pull handle" style="left:12px; top:323px; width:144px; height:97px;"></div>
    <h2 class="headline" style="left:80px; top:445px; font-size:19px; line-height:21px;">
      Historically<br>correct<br>window and<br>door <span class="accent">Hardware</span>
    </h2>
    <a class="cta cta-red" style="left:19px; top:553px; width:122px; height:27px;">Learn More</a>
  </section>
  <div class="size-label" style="left:316px; top:719px;">160x600</div>

  <!-- Medium rectangle 300x250 -->
  <section class="banner banner-rectangle" style="left:664px; top:455px; width:300px; height:250px;">
    <div class="banner-header" style="left:0; top:0; width:300px; height:66px;">
      <div class="brand" style="left:150px; top:23px;">
        <span class="brand-mark"></span>
        <span class="brand-name">Trueline Sash &amp; Renewal</span>
      </div>
    </div>
    <div class="product" role="img" aria-label="Polished brass door knob on round rose" style="left:22px; top:76px; width:96px; height:74px; border-radius:36px;"></div>
    <div class="product" role="img" aria-label="Brass sash lift, latch and pull handle" style="left:22px; top:155px; width:118px; height:78px;"></div>
    <h2 class="headline" style="left:217px; top:93px; font-size:17px; line-height:21px;">
      Historically<br>correct<br>window and<br>door <span class="accent">Hardware</span>
    </h2>
    <a class="cta cta-red" style="left:158px; top:186px; width:122px; height:27px;">Learn More</a>
  </section>
  <div class="size-label" style="left:814px; top:719px;">300x250</div>

  <!-- Leaderboard 728x90 -->
  <section class="banner banner-leaderboard" style="left:236px; top:773px; width:728px; height:88px;">
    <div class="banner-header" style="left:0; top:0; width:214px; height:88px;">
      <div class="brand" style="left:107px; top:17px;">
        <span class="brand-mark"></span>
        <span class="brand-name" style="font-size:16px;">Trueline Sash &amp; Renewal</span>
      </div>
      <a class="cta cta-grey" style="left:46px; top:51px; width:122px; height:27px;">Learn More</a>
    </div>
    <div class="product" role="img" aria-label="Brass door knob, pull handle, sash lift and latch" style="left:238px; top:5px; width:196px; height:78px;"></div>
    <h2 class="headline" style="left:575px; top:10px; font-size:22px; line-height:23px;">
      Historically correct<br>window and<br>door <span class="accent">Hardware</span>
    </h2>
  </section>
  <div class="size-label" style="left:600px; top:877px;">728x90</div>

</body>
</html>
```